Business card and stationery design

Harbour & Summit Planners is a leading event and conference design and management company.
Please view harbourandsummit.com.au

The business cards needs to convey:
- professionalism and competency
- exclusivity
- memorable experiences and quality

The business card needs to have the following aspects:
- double sided
- Full colour CMYK
- Printed on either high gloss matt card (designer to recommend)

For the business stationery we require:
- Letterhead with top banner and bottom footer
- A thank you card design
- a with compliments slip design
- a MS powerpoint and MS publisher client presentation slide design which includes cover page and then a standard presentation page
(Note- we do NOT require an envelope design- who sends letters these days!)

The company image is using the key colours of gold, silver and black.
A black background to the business card has been used before and is preferred although we are open to options.

Target Market(s)

High end corporations and businesses that require their events and conferences to be exceptionally well designed and managed

Industry/Entity Type

Business

Contact Information for Business Card

FRONT:

Darcy Whitlam
- Event and Conference Specialist

Mobile- +61 (0) 491 362 047
Office- 1300 586 917
darcyw@harbourandsummit.com.au

Web- harbourandsummit.com.au

BACK:

- Event and

Font styles to use
Other font styles liked:
• The logo designer used Trajan Pro Bold 3 for the font text in the logo

Requirements
Must have
• Amazing design of the following:
• - business card (double sided)
• - letterhead
• - client thank you card
• - powerpoint and publisher client presentation design files

```html
<!DOCTYPE html>
<html lang="en">
<head>
<meta charset="utf-8">
<title>Harbour &amp; Summit Planners – Business Card</title>
<link rel="stylesheet" href="https://fonts.googleapis.com/css2?family=Cinzel:wght@600&family=Open+Sans:wght@400;600&display=swap">
<style>
  :root {
    --backdrop: #4a4a4a;
    --card-black: #050505;
    --gold: #e3c060;
    --gold-deep: #b8902e;
    --silver: #d6d6d6;
    --silver-dark: #9a9a9a;
    --text-light: #f2f2f2;
    --text-dark: #1c1c1c;
    --rule: #bdbdbd;
  }
  * { margin: 0; padding: 0; box-sizing: border-box; }
  html, body { width: 1200px; height: 820px; overflow: hidden; }
  body { background: var(--backdrop); position: relative; font-family: "Open Sans", Arial, sans-serif; }

  .card {
    position: absolute; top: 257px; width: 477px; height: 274px;
    background: var(--card-black); overflow: hidden;
  }
  .card--front { left: 115px; }
  .card--back { left: 621px; }

  .brand {
    position: absolute; display: flex; align-items: center; gap: 8px;
    font-family: "Cinzel", "Times New Roman", serif; font-weight: 600;
    color: var(--silver); letter-spacing: 0.5px; white-space: nowrap;
  }
  .brand__dot { border-radius: 50%; background: var(--gold); flex: none; }
  .card--front .brand { left: 34px; top: 116px; font-size: 13px; }
  .card--front .brand__dot { width: 10px; height: 10px; }

  .rule { position: absolute; left: 33px; top: 162px; width: 253px; height: 1px; background: var(--rule); }

  .holder { position: absolute; left: 291px; top: 133px; }
  .holder__name {
    font-family: "Cinzel", "Times New Roman", serif; font-weight: 600;
    color: var(--gold); font-size: 16px; letter-spacing: 0.4px; line-height: 1.2;
  }
  .holder__role { color: var(--text-light); font-size: 10px; margin-top: 3px; }

  .contacts { position: absolute; left: 33px; top: 173px; list-style: none; }
  .contacts li {
    display: flex; align-items: center; gap: 6px; height: 20px;
    color: var(--text-light); font-size: 12px;
  }
  .contacts svg { width: 10px; height: 10px; fill: var(--gold); flex: none; }

  .footer-band { position: absolute; left: 0; top: 240px; width: 477px; height: 34px; }
  .web {
    position: absolute; left: 285px; top: 248px; line-height: 16px;
    font-size: 12px; color: var(--text-dark); white-space: nowrap;
  }

  .back-field {
    position: absolute; inset: 0;
    background:
      radial-gradient(circle at 50% 42%, rgba(60,60,60,0.55) 0%, rgba(20,20,20,0) 38%),
      radial-gradient(circle at 8% 60%, rgba(90,75,35,0.25) 0%, rgba(0,0,0,0) 22%),
      radial-gradient(circle at 92% 40%, rgba(90,75,35,0.22) 0%, rgba(0,0,0,0) 24%),
      radial-gradient(circle at 80% 90%, rgba(70,70,70,0.35) 0%, rgba(0,0,0,0) 25%),
      radial-gradient(circle at 20% 10%, rgba(70,70,70,0.3) 0%, rgba(0,0,0,0) 25%),
      #0a0a0a;
  }
  .card--back .brand {
    left: 0; right: 0; top: 180px; justify-content: center; font-size: 18px;
  }
  .card--back .brand__dot { width: 14px; height: 14px; }
</style>
</head>
<body>

<section class="card card--front" aria-label="Business card front">
  <div class="brand"><span class="brand__dot"></span>Harbour &amp; Summit Planners</div>
  <div class="rule"></div>
  <div class="holder">
    <p class="holder__name">DARCY WHITLAM</p>
    <p class="holder__role">Event and Conference Specialist</p>
  </div>
  <ul class="contacts">
    <li>
      <svg viewBox="0 0 10 10"><path d="M2 0.5 L3.6 0.5 L4.2 2.8 L3 3.6 Q4 5.8 6.4 7 L7.2 5.8 L9.5 6.4 L9.5 8 Q9.5 9.5 8 9.5 Q0.5 9 0.5 2 Q0.5 0.5 2 0.5 Z"/></svg>
      1300 586 917
    </li>
    <li>
      <svg viewBox="0 0 10 10"><path d="M2.5 0 H7.5 V10 H2.5 Z M3.3 1 V8 H6.7 V1 Z"/></svg>
      +61 (0) 491 362 047
    </li>
    <li>
      <svg viewBox="0 0 10 10"><path d="M0 2 H10 V8.5 H0 Z M0.8 2.6 L5 5.6 L9.2 2.6 Z" fill-rule="evenodd"/></svg>
      darcyw@harbourandsummit.com.au
    </li>
  </ul>
  <svg class="footer-band" viewBox="0 0 477 34" aria-hidden="true">
    <defs>
      <linearGradient id="goldBar" x1="0" x2="1" y1="0" y2="0">
        <stop offset="0" stop-color="#b8902e"/>
        <stop offset="0.5" stop-color="#f0d47a"/>
        <stop offset="1" stop-color="#b8902e"/>
      </linearGradient>
      <linearGradient id="silverBar" x1="0" x2="1" y1="0" y2="1">
        <stop offset="0" stop-color="#8e8e8e"/>
        <stop offset="0.45" stop-color="#f4f4f4"/>
        <stop offset="1" stop-color="#bcbcbc"/>
      </linearGradient>
    </defs>
    <polygon points="0,11 262,11 256,18 0,18" fill="url(#goldBar)"/>
    <polygon points="0,18 255,18 252,21 0,21" fill="#8a8a8a"/>
    <polygon points="270,1 477,1 477,34 254,34" fill="url(#silverBar)"/>
  </svg>
  <span class="web">harbourandsummit.com.au</span>
</section>

<section class="card card--back" aria-label="Business card back">
  <div class="back-field" role="img" aria-label="Dark background where faint grey and gold bubbles are scattered"></div>
  <div class="brand"><span class="brand__dot"></span>Harbour &amp; Summit Planners</div>
</section>

</body>
</html>
```